Technology Enablement - One Pager

I need (2) one pager piece of marketing collateral to use as outreach for a service offering. The one pager must have a strong call to action, highlight the pain points the service solves.

```html
<!DOCTYPE html>
<html lang="en">
<head>
<meta charset="UTF-8">
<title>Technology Enablement for Trades</title>
<link href="https://fonts.googleapis.com/css2?family=Open+Sans:wght@400;600;700;800&family=Montserrat:wght@500;700&display=swap" rel="stylesheet">
<style>
  :root{
    --navy:#0d2f5c;
    --navy-deep:#09274f;
    --yellow:#fdd35a;
    --yellow-soft:#ffdc6e;
    --gold-text:#f7c843;
    --ink:#1b1b1b;
    --white:#ffffff;
    --grey:#dedede;
    --backdrop:#e6e6e6;
  }
  *{box-sizing:border-box;margin:0;padding:0}
  html,body{width:1200px;height:1200px;overflow:hidden}
  body{background:var(--backdrop);font-family:"Open Sans",Arial,sans-serif;color:var(--ink);position:relative}
  .flyer{position:absolute;left:190px;top:20px;width:820px;height:1160px;background:var(--white);overflow:hidden;box-shadow:0 4px 18px rgba(0,0,0,.12)}
  .sec{position:absolute;left:0;width:820px}
  ul{list-style:none}
  li{display:flex;align-items:center;gap:5px}

  /* header */
  .header{top:0;height:161px;text-align:center;padding-top:19px}
  .header .kicker{font-size:18px;font-weight:700;color:var(--navy);line-height:1.2}
  .header .trades{font-size:15px;line-height:1.3}
  .header h1{font-size:24.5px;font-weight:800;color:var(--navy);line-height:1.3}
  .header .lede{font-size:23px;line-height:1.28;font-weight:400}

  /* reality */
  .reality{top:161px;height:231px;background:var(--navy);color:var(--white)}
  .tab{position:absolute;left:0;top:0;height:31px;width:253px;background:var(--yellow);clip-path:polygon(0 0,100% 0,88% 100%,0 100%);padding-left:24px;font-size:16.5px;font-weight:700;color:var(--navy);line-height:31px}
  .reality .body{position:absolute;left:22px;top:36px;font-size:10.6px;line-height:13.2px}
  .reality .sub{color:var(--gold-text);font-weight:600;margin:5px 0 3px}
  .reality li{height:15.2px}
  .reality .close{margin-top:5px}
  .box{width:9px;height:9px;border:1.2px solid currentColor;display:inline-flex;align-items:center;justify-content:center;font-size:7px;line-height:1;flex:none}
  .reality .box{color:var(--gold-text)}
  .gears-art{position:absolute;right:0;top:10px;width:290px;height:215px;background:radial-gradient(ellipse at 65% 55%,#19b6ef 0%,#0c6fb8 35%,rgba(13,47,92,0) 72%)}

  /* approach */
  .approach{top:397px;height:177px;background:linear-gradient(90deg,var(--yellow) 0%,var(--yellow-soft) 50%,var(--yellow) 100%)}
  .approach h2{font-size:16px;font-weight:700;margin-bottom:3px}
  .col-left{position:absolute;left:22px;top:12px;width:380px;font-size:10.6px;line-height:13.2px}
  .col-right{position:absolute;left:532px;top:12px;width:280px;font-size:10.6px;line-height:13.2px}
  .divider{position:absolute;left:448px;top:16px;width:3px;height:145px;background:var(--navy-deep)}
  .circ{width:9px;height:9px;border:1px solid var(--ink);border-radius:50%;display:inline-flex;align-items:center;justify-content:center;font-size:6px;flex:none}
  .approach li{height:15.2px}
  .gap{height:5px}

  /* product */
  .product{top:574px;height:65px;text-align:center;padding-top:12px}
  .product h2{font-size:22px;font-weight:700;color:var(--navy);line-height:1.25}
  .product p{font-size:10.5px}

  .deal{top:639px;height:160px}
  .review{position:absolute;left:0;top:0;width:410px;height:160px;background:var(--navy);color:var(--white);padding:14px 0 0 23px;font-size:10.6px;line-height:15.2px}
  .review h3,.receive h3{font-size:16.5px;font-weight:700;line-height:1.3;margin-bottom:1px}
  .review h3{color:var(--gold-text)}
  .receive{position:absolute;left:410px;top:0;width:410px;height:160px;background:var(--yellow);padding:14px 0 0 103px;font-size:10.6px;line-height:13.2px}
  .receive h3{color:var(--navy)}
  .receive li{height:13.2px}
  .tick{font-size:10px;flex:none}
  .badge{position:absolute;left:360px;top:28px;width:104px;height:104px;border-radius:50%;border:4px solid var(--white);background:radial-gradient(circle at 55% 45%,#d9a635 0%,#6b4a1a 45%,#1d140a 85%);box-shadow:0 0 0 1px rgba(0,0,0,.2)}

  /* lower */
  .lower{top:799px;height:361px;background:var(--grey)}
  .who{position:absolute;left:0;top:0;width:410px;height:92px;background:var(--white);padding:5px 0 0 23px;font-size:10.6px;line-height:15.2px}
  .who h3,.why h3{font-size:16px;font-weight:700;color:var(--navy);line-height:1.35}
  .fill{background:var(--navy);color:var(--white);width:9px;height:9px;display:inline-flex;align-items:center;justify-content:center;font-size:7px;flex:none}
  .photo-team{position:absolute;left:0;top:92px;width:410px;height:120px;background:linear-gradient(90deg,#2a3b52 0%,#a8c3dc 45%,#e9eef3 70%,#c9a98e 100%);border-right:3px solid var(--yellow);border-bottom:3px solid var(--yellow)}
  .photo-lab{position:absolute;left:412px;top:0;width:408px;height:94px;background:linear-gradient(90deg,#2c4665 0%,#8aa9c6 35%,#c8d3dc 60%,#1f3148 100%);border-bottom:3px solid var(--navy)}
  .why{position:absolute;left:412px;top:97px;width:408px;height:115px;padding:2px 0 0 31px;font-size:10.6px;line-height:13.2px}
  .why .gap{height:4px}
  .why li{height:15.2px}
  .tagline{position:absolute;left:0;top:228px;width:820px;text-align:center;font-family:"Montserrat",Arial,sans-serif;font-size:16px;font-weight:500}
  .cta{position:absolute;left:93px;top:276px;width:634px;height:45px;border-radius:14px;background:var(--navy-deep);color:var(--gold-text);font-family:"Montserrat",Arial,sans-serif;font-weight:700;font-size:19px;display:flex;align-items:center;justify-content:center;letter-spacing:-.2px}
</style>
</head>
<body>
<main class="flyer">
  <header class="sec header">
    <p class="kicker">Technology Enablement for Trades</p>
    <p class="trades">(Electrical, Plumbing, HVAC, Mechanical, Construction)</p>
    <h1>Your jobs are physical. Your problems aren’t.</h1>
    <p class="lede">We help trade businesses fix the tech<br>and workflows behind the work.</p>
  </header>

  <section class="sec reality">
    <div class="tab">The Reality in the Trades</div>
    <div class="body">
      <p>Trade companies rely on technology more than ever —<br>even if they don’t call it “IT.”<br>Scheduling. Estimating. Job tracking. Invoicing. Payroll. Field apps.<br>Most of it works… kind of.</p>
      <p class="sub">Common frustrations:</p>
      <ul>
        <li><span class="box">✓</span>Office and field systems don’t line up</li>
        <li><span class="box">✓</span>Dispatch process is manual or inefficient.</li>
        <li><span class="box">✓</span>Jobs get quoted one way and invoiced another</li>
        <li><span class="box">✓</span>Information is stuck in texts, notebooks, or someone’s phone</li>
        <li><span class="box">✓</span>Admin work grows faster than revenue</li>
        <li><span class="box">✓</span>Technology decisions fall to “whoever knows computers”</li>
      </ul>
      <p class="close">The work gets done — but it takes more effort than it should.</p>
    </div>
    <div class="gears-art" role="img" aria-label="Glowing blue gears and circuit lines illustration"></div>
  </section>

  <section class="sec approach">
    <div class="col-left">
      <h2>What We Do</h2>
      <p>We help trade companies simplify operations using technology they already depend on.</p>
      <div class="gap"></div>
      <p>Corvanta focuses on:</p>
      <div class="gap"></div>
      <ul>
        <li><span class="circ">✓</span>How work flows from quote → job → invoice → reporting</li>
        <li><span class="circ">✓</span>How office and field tools connect (or don’t)</li>
        <li><span class="circ">✓</span>Where manual steps create delays, rework, or missed revenue</li>
        <li><span class="circ">✓</span>Why tools aren’t being fully used by crews or admin staff</li>
      </ul>
      <div class="gap"></div>
      <p>This is about making the business easier to run — not selling IT jargon.</p>
    </div>
    <div class="divider"></div>
    <div class="col-right">
      <h2>Why Trades Like Our Approach</h2>
      <ul>
        <li><span class="circ">✓</span>Low-risk, practical, and clear</li>
        <li><span class="circ">✓</span>No pressure to replace systems</li>
        <li><span class="circ">✓</span>No requirement to change IT providers</li>
        <li><span class="circ">✓</span>Focused on productivity, not tech for tech’s sake</li>
      </ul>
      <div class="gap"></div>
      <p>We earn trust by fixing real problems first.</p>
    </div>
  </section>

  <section class="sec product">
    <h2>Product 1: Trades Technology Enablement Assessment</h2>
    <p>A 2–4 week, stand-alone assessment built specifically for trades</p>
  </section>

  <section class="sec deal">
    <div class="review">
      <h3>We review:</h3>
      <ul>
        <li><span class="tick">✓</span>Job management workflows</li>
        <li><span class="tick">✓</span>Quoting&nbsp;&nbsp;&nbsp; scheduling&nbsp;&nbsp;&nbsp; invoicing flow</li>
        <li><span class="tick">✓</span>Field tools and adoption gaps</li>
        <li><span class="tick">✓</span>Office vs field handoffs</li>
        <li><span class="tick">✓</span>Reporting visibility (jobs, labour, margins)</li>
        <li><span class="tick">✓</span>Security and data risks (without fear tactics)</li>
      </ul>
    </div>
    <div class="receive">
      <h3>You receive:</h3>
      <p>A Trades-Specific Improvement Roadmap showing:</p>
      <div class="gap"></div>
      <ul>
        <li><span class="tick">✓</span>Where time and money are being lost</li>
        <li><span class="tick">✓</span>What to fix first</li>
        <li><span class="tick">✓</span>What can wait</li>
        <li><span class="tick">✓</span>Where automation or integration actually pays off</li>
      </ul>
      <div class="gap"></div>
      <p>Price: <strong>$2,500</strong><br>Straightforward. No obligation beyond the assessment.</p>
    </div>
    <div class="badge" role="img" aria-label="Yellow robotic arm photograph in a circle"></div>
  </section>

  <section class="sec lower">
    <div class="who">
      <h3>Who This Is For</h3>
      <ul>
        <li><span class="fill">✓</span>Electrical, plumbing, HVAC, mechanical, GC, and construction firms</li>
        <li><span class="fill">✓</span>Owners feeling buried in admin</li>
        <li><span class="fill">✓</span>Companies growing past “winging it”</li>
        <li><span class="fill">✓</span>Trades relying on multiple apps that don’t work well together</li>
      </ul>
    </div>
    <div class="photo-team" role="img" aria-label="Photograph of office staff working together"></div>
    <div class="photo-lab" role="img" aria-label="Photograph of a team reviewing a design on a monitor"></div>
    <div class="why">
      <h3>Why Start With an Assessment</h3>
      <p>Because guessing costs more than clarity.<br>This gives you:</p>
      <div class="gap"></div>
      <ul>
        <li><span class="fill">✓</span>A clear plan instead of piecemeal fixes</li>
        <li><span class="fill">✓</span>Confidence before spending on new tools</li>
        <li><span class="fill">✓</span>A roadmap aligned to how trades actually work</li>
      </ul>
    </div>
    <p class="tagline">Fix the systems behind the scenes — so the work runs smoother on site.</p>
    <div class="cta">BOOK A TRADES TECHNOLOGY ENABLEMENT ASSESSMENT</div>
  </section>
</main>
</body>
</html>
```